Miss Dazzle Wren Flyer

Hi, Thank you for doing such a great job! I would like you to work with me on this flyer but give me a couple of option designs that I could choose from. To be honest im still a hundred per cent in what contents I want on this flyer but here it is. This is a double sided flyer!

One side is Miss Dazzle Wren and the other side is Harbourline Roaming Glow & Beauty.

I was thinking with Miss Dazzle Wren I could have some slogan like Lets Party.... (something like that) I was thinking balloons etc. Also I have 4 boxes that I want to use with pictures with a little brief description in paragrapth order.

I don't have the description yet but will be writing it this weekend. I can upload later as I would like to get the design started. I would like you to use Spoil You Soirees, Twirl of Lilac Ballet Party, Dj Funk Beat Dance Party and lastly Tiny Cup Clever Wren Party. You will see I have attached a photo of a ballet girl, hip hop photo, high tea photo and a pamper photo of two girls. These pictures are used in conjunction with each party theme. I will also need my number in large and including another number as well (I think) I will get back to that. as well as a email address ( I will also get back to you with that) my web address and a facebook thing to like.

Harbourline Roaming Glow & Beauty

Basically this side is about our Adult Pamper Party. I would like to say something that I will forward to you. If wil only be breif, and a picture and promoting how the host received a free skin care kit of choice valued at $180 for hosting etc and maybe down the bottom of the page I could also in point form put my other services. I If you can start on Miss Dazzle Wren that would be a good start and I can get back to you with more information on this one. This is a gift to me and they want me to pay for it now when I wasn't prepared with all my information for you. so please forgive me.

I was thinking this may be just for a A5 size but at some stage I will print both on a4 as well as poster size if this is possible.

You are probably confused as I am too. I will forward miss dazzle wren pictures in order and then one for Harbourline roaming glow and beauty (but I have another one coming on Monday) I will email you as necessary with more of my wording I need.

I know less is better so im trying not to put to much for Harbourline roaming but I think really like to talk a bit more about party options for miss d w .

I will be going onto picsvaultly now to see if I can find another appro photo for pamper parties then apposed to one I sent. Im sure you will be not understanding my contents as im totally not prepared but I hope you can get started . And once again thank you very very much.

Target Market(s)

parents with children for miss dazzle wren and women over the age of thirty for adult pamper parties on the opposite flyer

Industry/Entity Type

Adult

Requirements
Must have
• the last image of lady with mask on half her face . I would like that picture on Harbourline roming glow and beauty side for pamper parties please. you can choose to ignore the girl with champagn glass if you wish as I need to put a picture of what thehost gets and I will upload that one within the next two days.
Should not have
• under the logo Harbourline roaming glow and beauty I want the words healthier looking skin taken out please

```html
<!DOCTYPE html>
<html lang="en">
<head>
<meta charset="utf-8">
<title>Harbourline Roaming Glow &amp; Beauty – Adult Pamper Party Flyer</title>
<link href="https://fonts.googleapis.com/css2?family=Comfortaa:wght@500;700&family=Gabriela&display=swap" rel="stylesheet">
<style>
  :root {
    --page-bg: #f1f1f1;
    --frame: #cfdcda;
    --paper: #ffffff;
    --pink: #e1468f;
    --plum: #8a3a6c;
    --soft-text: #c9a3b6;
    --stitch: #e890b4;
  }
  html, body {
    margin: 0;
    padding: 0;
    width: 1200px;
    height: 1000px;
    overflow: hidden;
    background: var(--page-bg);
  }
  .flyer {
    position: absolute;
    left: 288px;
    top: 60px;
    width: 622px;
    height: 882px;
    background: var(--frame);
    box-shadow: 0 2px 6px rgba(0,0,0,0.18);
  }
  .flyer__paper {
    position: absolute;
    left: 10px;
    top: 16px;
    width: 570px;
    height: 848px;
    background: var(--paper);
  }
  .flyer__stitch {
    position: absolute;
    left: 598px;
    top: 0;
    height: 882px;
    width: 6px;
  }
  .hero-photo {
    position: absolute;
    left: 2px;
    top: 16px;
    width: 344px;
    height: 536px;
    background: linear-gradient(160deg, #3a2a22 0%, #a97c62 30%, #e3c1a6 55%, #f3ece4 100%);
  }
  .brand {
    position: absolute;
    left: 346px;
    top: 48px;
    width: 234px;
    text-align: center;
    font-family: "Gabriela", serif;
  }
  .brand__mark {
    display: block;
    width: 14px;
    height: 14px;
    margin: 0 auto 10px;
    background: var(--pink);
  }
  .brand__name {
    font-family: "Gabriela", serif;
    font-size: 19px;
    line-height: 1.25;
    color: var(--plum);
    margin: 0;
  }
  .contact {
    position: absolute;
    left: 346px;
    top: 188px;
    width: 234px;
    text-align: center;
  }
  .contact__phone {
    font-family: "Comfortaa", sans-serif;
    font-weight: 700;
    font-size: 22px;
    color: var(--plum);
    letter-spacing: 1px;
    display: flex;
    align-items: center;
    justify-content: center;
    gap: 6px;
  }
  .contact__email {
    font-family: "Gabriela", serif;
    font-size: 10.5px;
    color: var(--soft-text);
    margin-top: 6px;
  }
  .headline {
    position: absolute;
    left: 356px;
    top: 286px;
    margin: 0;
    font-family: "Comfortaa", sans-serif;
    font-weight: 700;
    font-size: 54px;
    line-height: 90px;
    color: var(--pink);
    letter-spacing: -1px;
  }
  .headline span { display: block; }
  .offer {
    position: absolute;
    left: 40px;
    top: 580px;
    width: 540px;
    margin: 0;
    font-family: "Gabriela", serif;
    font-size: 31px;
    line-height: 60px;
    color: var(--pink);
    font-weight: 400;
    white-space: nowrap;
  }
  .tagline-art {
    position: absolute;
    left: 38px;
    top: 738px;
    width: 90px;
    height: 90px;
    background: radial-gradient(circle, #fbe3ee 0%, #f6c9dd 100%);
    border-radius: 8px;
  }
  .services {
    position: absolute;
    left: 152px;
    top: 734px;
    width: 420px;
    font-family: "Gabriela", serif;
    color: var(--pink);
    white-space: nowrap;
  }
  .services__title {
    font-size: 16px;
    margin: 0 0 4px;
    font-weight: 400;
  }
  .services__list {
    font-size: 13px;
    line-height: 26px;
    margin: 0;
  }
</style>
</head>
<body>
  <article class="flyer">
    <div class="flyer__paper"></div>
    <svg class="flyer__stitch" viewBox="0 0 6 882" aria-hidden="true">
      <line x1="3" y1="0" x2="3" y2="882" stroke="var(--stitch)" stroke-width="1.2" stroke-dasharray="3 3"/>
    </svg>

    <div class="hero-photo" role="img" aria-label="Photo of a woman relaxing with a white facial mask being brushed onto half her face, hair wrapped in a towel"></div>

    <header class="brand">
      <span class="brand__mark"></span>
      <p class="brand__name">Harbourline Roaming<br>Glow &amp; Beauty</p>
    </header>

    <div class="contact">
      <div class="contact__phone">
        <svg width="16" height="16" viewBox="0 0 24 24" aria-hidden="true">
          <path d="M6.6 10.8a15 15 0 0 0 6.6 6.6l2.2-2.2a1 1 0 0 1 1-.25 11.4 11.4 0 0 0 3.6.57 1 1 0 0 1 1 1V20a1 1 0 0 1-1 1A17 17 0 0 1 3 4a1 1 0 0 1 1-1h3.5a1 1 0 0 1 1 1c0 1.25.2 2.450.57 3.6a1 1 0 0 1-.25 1z" fill="var(--plum)"/>
        </svg>
        0400 51 7373
      </div>
      <div class="contact__email">harbourlineroamingglow@mailnest.com</div>
    </div>

    <h1 class="headline"><span>adult</span><span>pamper</span><span>party</span></h1>

    <p class="offer">Host will receive a free skincare<br>kit of choice valued at $180 !</p>

    <div class="tagline-art" role="img" aria-label="Decorative heart emblem with a skin-love slogan"></div>

    <section class="services">
      <h2 class="services__title">Harbourline Roaming Glow &amp; Beauty also offers:</h2>
      <p class="services__list">Facials &amp; Peels, Microdermabrasion, 10 Minute Liquid<br>Facelifting, Oxygen Infustion, Derma Rolling / Skin Needling,<br>Tinting &amp; Waxing, Skincare Products</p>
    </section>
  </article>
</body>
</html>
```